Desk Allies Business Card

Contact Information for Business Card

Jaakko Virtanola
Managing Director

3/47 Darrow Lane Belmont ACT 2915

Tel: +61 02 6187 4326
Mob: +61 0432 715 649

Email: jaakko@deskallies-example.com.au
Web: www.deskallies-example.com.au

Colors

Designer to choose colors to be used in the design.

Requirements
Must have
• Logo, Name, Title, Address, Telephone, Mobile, Email Address and Website
• "Desk Ally Worldwide Pty Ltd"

```html
<!DOCTYPE html>
<html lang="en">
<head>
<meta charset="utf-8">
<title>Desk Allies Business Cards</title>
<link rel="stylesheet" href="https://fonts.googleapis.com/css2?family=Roboto:wght@400;500;700&family=Roboto+Condensed:wght@400;700&display=swap">
<style>
  :root {
    --page: #e9e7e4;
    --card-dark: #17191b;
    --card-light: #f3f3f2;
    --brand-blue: #1e6fb5;
    --ink-white: #ffffff;
    --ink-grey: #55585c;
    --rule: #4a4d51;
  }
  * { box-sizing: border-box; margin: 0; padding: 0; }
  html, body { width: 1200px; height: 1060px; overflow: hidden; }
  body { background: var(--page); position: relative; font-family: "Roboto", sans-serif; }

  .card {
    position: absolute;
    width: 465px;
    height: 265px;
    background: var(--card-dark);
    color: var(--ink-white);
    overflow: hidden;
  }
  .card--light { background: var(--card-light); }

  .identity {
    position: absolute;
    right: 253px;
    top: 97px;
    height: 68px;
    display: flex;
    flex-direction: column;
    justify-content: center;
    align-items: flex-end;
    text-align: right;
    white-space: nowrap;
  }
  .identity__name {
    font-family: "Roboto Condensed", sans-serif;
    font-weight: 700;
    font-size: 23px;
    line-height: 1;
    color: var(--brand-blue);
    text-transform: uppercase;
  }
  .identity__title {
    font-family: "Roboto Condensed", sans-serif;
    font-weight: 700;
    font-size: 11.5px;
    margin-top: 4px;
    text-transform: uppercase;
  }
  .divider {
    position: absolute;
    left: 233px;
    top: 97px;
    width: 1px;
    height: 68px;
    background: var(--rule);
  }
  .contacts {
    position: absolute;
    left: 250px;
    top: 101px;
    list-style: none;
    font-size: 11.5px;
    line-height: 15px;
    white-space: nowrap;
  }
  .contacts li { display: flex; align-items: center; gap: 6px; }
  .icon { width: 10px; height: 10px; fill: var(--brand-blue); flex: none; }

  .card--no-title .identity { right: 235px; }
  .card--no-title .divider { left: 243px; }
  .card--no-title .contacts { left: 256px; }

  .address {
    position: absolute;
    left: 0; right: 0;
    top: 221px;
    display: flex;
    justify-content: center;
    align-items: center;
    gap: 4px;
    font-family: "Roboto Condensed", sans-serif;
    font-size: 12.5px;
    white-space: nowrap;
  }
  .address .icon { width: 9px; height: 11px; }

  .brand {
    position: absolute;
    left: 0; right: 0;
    top: 102px;
    display: flex;
    justify-content: center;
    align-items: center;
    gap: 12px;
  }
  .brand__dot {
    width: 44px; height: 44px;
    border-radius: 50%;
    background: var(--brand-blue);
  }
  .brand__name {
    font-family: "Roboto", sans-serif;
    font-weight: 500;
    font-size: 27px;
    letter-spacing: 0.5px;
    color: var(--brand-blue);
    text-transform: uppercase;
  }
  .website {
    position: absolute;
    left: 0; right: 0;
    top: 217px;
    text-align: center;
    font-size: 11.5px;
    letter-spacing: 5.2px;
    color: var(--ink-white);
  }
  .card--light .website { color: var(--ink-grey); }
</style>
</head>
<body>
<svg width="0" height="0" style="position:absolute" aria-hidden="true">
  <defs>
    <symbol id="i-phone" viewBox="0 0 24 24"><path d="M6.6 10.8a15.1 15.1 0 0 0 6.6 6.6l2.2-2.2a1 1 0 0 1 1-.25 11.4 11.4 0 0 0 3.6.6 1 1 0 0 1 1 1V20a1 1 0 0 1-1 1A17 17 0 0 1 3 4a1 1 0 0 1 1-1h3.5a1 1 0 0 1 1 1c0 1.25.2 2.45.6 3.6a1 1 0 0 1-.25 1z"/></symbol>
    <symbol id="i-mobile" viewBox="0 0 24 24"><path d="M7 1h10a2 2 0 0 1 2 2v18a2 2 0 0 1-2 2H7a2 2 0 0 1-2-2V3a2 2 0 0 1 2-2zm0 3v14h10V4z"/></symbol>
    <symbol id="i-mail" viewBox="0 0 24 24"><path d="M2 6l10 6 10-6v12H2z"/><path d="M2 4h20l-10 6z"/></symbol>
    <symbol id="i-globe" viewBox="0 0 24 24"><path d="M12 2a10 10 0 1 0 0 20 10 10 0 0 0 0-20zm-1 17.9A8 8 0 0 1 4.2 10L9 15v1a2 2 0 0 0 2 2zm6.9-2.5A2 2 0 0 0 16 16h-1v-3a1 1 0 0 0-1-1H8v-2h2a1 1 0 0 0 1-1V7h2a2 2 0 0 0 2-2v-.4a8 8 0 0 1 2.9 12.8z"/></symbol>
    <symbol id="i-pin" viewBox="0 0 20 26"><path d="M10 0a9 9 0 0 0-9 9c0 7 9 17 9 17s9-10 9-17a9 9 0 0 0-9-9zm0 13a4 4 0 1 1 0-8 4 4 0 0 1 0 8z"/></symbol>
  </defs>
</svg>

<article class="card card--front" style="left:110px;top:93px">
  <div class="identity">
    <h2 class="identity__name">Jaakko Virtanola</h2>
    <p class="identity__title">Managing Director</p>
  </div>
  <div class="divider"></div>
  <ul class="contacts">
    <li><svg class="icon"><use href="#i-phone"/></svg>+61 02 6187 4326</li>
    <li><svg class="icon"><use href="#i-mobile"/></svg>+61 0432 715 649</li>
    <li><svg class="icon"><use href="#i-mail"/></svg>jaakko@deskallies-example.com.au</li>
    <li><svg class="icon"><use href="#i-globe"/></svg>www.deskallies-example.com.au</li>
  </ul>
  <p class="address"><svg class="icon"><use href="#i-pin"/></svg>Desk Ally Worldwide Pty Ltd, 3/47 Darrow Lane Belmont ACT 2915</p>
</article>

<article class="card card--front" style="left:608px;top:93px">
  <div class="identity">
    <h2 class="identity__name">Rowan Ashbury</h2>
    <p class="identity__title">Business Development Manager</p>
  </div>
  <div class="divider"></div>
  <ul class="contacts">
    <li><svg class="icon"><use href="#i-phone"/></svg>+61 02 6187 4326</li>
    <li><svg class="icon"><use href="#i-mobile"/></svg>0455 218 704</li>
    <li><svg class="icon"><use href="#i-mail"/></svg>rowan@deskallies-example.com.au</li>
    <li><svg class="icon"><use href="#i-globe"/></svg>www.deskallies-example.com.au</li>
  </ul>
  <p class="address"><svg class="icon"><use href="#i-pin"/></svg>Desk Ally Worldwide Pty Ltd, 3/47 Darrow Lane Belmont ACT 2915</p>
</article>

<article class="card card--front card--no-title" style="left:110px;top:396px">
  <div class="identity">
    <h2 class="identity__name">Lukas Brennwald</h2>
  </div>
  <div class="divider"></div>
  <ul class="contacts">
    <li><svg class="icon"><use href="#i-phone"/></svg>+61 02 6187 4326</li>
    <li><svg class="icon"><use href="#i-mobile"/></svg>0461 392 587</li>
    <li><svg class="icon"><use href="#i-mail"/></svg>lukas@deskallies-example.com.au</li>
    <li><svg class="icon"><use href="#i-globe"/></svg>www.deskallies-example.com.au</li>
  </ul>
  <p class="address"><svg class="icon"><use href="#i-pin"/></svg>Desk Ally Worldwide Pty Ltd, 3/47 Darrow Lane Belmont ACT 2915</p>
</article>

<article class="card card--front card--no-title" style="left:608px;top:396px">
  <div class="identity">
    <h2 class="identity__name">Eero Virtanola</h2>
  </div>
  <div class="divider"></div>
  <ul class="contacts">
    <li><svg class="icon"><use href="#i-phone"/></svg>+61 02 6187 4326</li>
    <li><svg class="icon"><use href="#i-mobile"/></svg>0423 846 115</li>
    <li><svg class="icon"><use href="#i-mail"/></svg>eero@deskallies-example.com.au</li>
    <li><svg class="icon"><use href="#i-globe"/></svg>www.deskallies-example.com.au</li>
  </ul>
  <p class="address"><svg class="icon"><use href="#i-pin"/></svg>Desk Ally Worldwide Pty Ltd, 3/47 Darrow Lane Belmont ACT 2915</p>
</article>

<article class="card card--back card--light" style="left:112px;top:705px">
  <div class="brand"><span class="brand__dot"></span><span class="brand__name">Desk Allies</span></div>
  <p class="website">www.deskallies-example.com.au</p>
</article>

<article class="card card--back" style="left:611px;top:705px">
  <div class="brand"><span class="brand__dot"></span><span class="brand__name">Desk Allies</span></div>
  <p class="website">www.deskallies-example.com.au</p>
</article>
</body>
</html>
```